New lease of life for a tired Country Pub menu, QLD

I need to refresh my menus with updated prices. The menus need to be A4 (the menus are laminated and handed out over the bar. I'd like to include our logo. I will upload our existing menus as well as the new prices. The design should be humble yet stylish if that's ok, please

Target Market(s)

Locals, travellers and workers

Industry/Entity Type

Hospitality, Quintessential Country pub

Font styles to use
Sans Serif

Colors

Designer to choose colors to be used in the design.

Requirements
Must have
• as we run different menus on different nights
Nice to have
• our logo

```html
<!DOCTYPE html>
<html lang="en">
<head>
<meta charset="utf-8">
<title>Hotel Whitmore – Parmis Menu</title>
<link href="https://fonts.googleapis.com/css2?family=Fira+Sans:wght@500;600;700&display=swap" rel="stylesheet">
<style>
  :root {
    --backdrop: #b3b3b3;
    --board: #000000;
    --ink-light: #ececec;
    --tag: #e6e6e6;
    --ink-dark: #111111;
    --frame: #e6e6e6;
  }
  * { margin: 0; padding: 0; box-sizing: border-box; }
  html, body {
    width: 890px; height: 1200px; overflow: hidden;
    background: var(--backdrop);
    font-family: "Fira Sans", Arial, sans-serif;
  }
  .page { position: relative; width: 890px; height: 1200px; }
  .menu-board {
    position: absolute; left: 71px; top: 71px;
    width: 747px; height: 1058px;
    background: var(--board);
    border-radius: 27px;
    overflow: hidden;
    box-shadow: 8px 10px 10px rgba(0,0,0,0.25);
  }
  .footer-band { position: absolute; left: 0; top: 0; }
  .footer-note {
    position: absolute; left: 0; right: 0; top: 1024px;
    text-align: center; font-weight: 700; font-size: 14px;
    color: var(--ink-dark); letter-spacing: 0.2px;
  }
  .frames { position: absolute; left: 0; top: 0; }
  .venue-name {
    position: absolute; left: 0; width: 890px; top: 112px;
    text-align: center; color: var(--ink-light);
    font-weight: 600; font-size: 21px; line-height: 22px;
    letter-spacing: 0.5px;
  }
  .menu-title {
    position: absolute; left: 0; width: 890px; top: 196px;
    text-align: center; color: var(--ink-light);
    font-weight: 700; font-size: 44px; line-height: 56px;
  }
  .section-label {
    position: absolute; height: 22px;
    background: var(--tag); border-radius: 11px;
    color: var(--ink-dark); font-weight: 700; font-size: 17px;
    letter-spacing: 6px; text-indent: 6px;
    display: flex; align-items: center; justify-content: center;
  }
  .item {
    position: absolute; left: 137px; height: 36px;
    display: flex; align-items: center;
    color: var(--ink-light); font-weight: 600; font-size: 25px;
  }
  .price {
    position: absolute; left: 679px; width: 139px; height: 37px;
    background: var(--tag); border-radius: 5px 0 0 5px;
    color: var(--ink-dark); font-weight: 700; font-size: 28px;
    display: flex; align-items: center; padding-left: 8px;
  }
</style>
</head>
<body>
<div class="page">
  <div class="menu-board">
    <svg class="footer-band" width="747" height="1058" viewBox="0 0 747 1058">
      <path d="M0,1058 L0,1055 Q373.5,970 747,1055 L747,1058 Z" fill="var(--tag)"/>
    </svg>
    <p class="footer-note">HALF/ HALF NOT AVAILABLE</p>
  </div>

  <svg class="frames" width="890" height="1200" viewBox="0 0 890 1200" fill="none" stroke="var(--frame)" stroke-width="2">
    <path d="M125.5,293 H388 V303 A14 14 0 0 0 402 317 H488 A14 14 0 0 0 502 303 V293 H763.5 A14 14 0 0 1 777.5 307 V638 A14 14 0 0 1 763.5 652 H125.5 A14 14 0 0 1 111.5 638 V307 A14 14 0 0 1 125.5 293 Z"/>
    <path d="M125.5,699 H363 V709 A14 14 0 0 0 377 723 H512 A14 14 0 0 0 526 709 V699 H763.5 A14 14 0 0 1 777.5 713 V1043.5 A14 14 0 0 1 763.5 1057.5 H125.5 A14 14 0 0 1 111.5 1043.5 V713 A14 14 0 0 1 125.5 699 Z"/>
  </svg>

  <h2 class="venue-name">HOTEL<br>WHITMORE</h2>
  <h1 class="menu-title">PARMIS MENU</h1>

  <div class="section-label" style="left:401px; top:282px; width:88px;">BEEF</div>
  <div class="item" style="top:328px;">BEEF PARMI</div>
  <div class="price" style="top:328px;">$30.00</div>
  <div class="item" style="top:391px;">AUSSIE BEEF PARMIGIANA</div>
  <div class="price" style="top:391px;">$30.95</div>
  <div class="item" style="top:454px;">BEEF HAWAIIAN PARMI</div>
  <div class="price" style="top:454px;">$30.95</div>
  <div class="item" style="top:517px;">BEEF HOT AND SPICY PARMI</div>
  <div class="price" style="top:517px;">$30.95</div>
  <div class="item" style="top:580px;">BEEF MEATLOVERS PARMI</div>
  <div class="price" style="top:580px;">$30.95</div>

  <div class="section-label" style="left:376px; top:689px; width:138px;">CHICKEN</div>
  <div class="item" style="top:734px;">CHICKEN PARMI</div>
  <div class="price" style="top:734px;">$29.99</div>
  <div class="item" style="top:797px;">AUSSIE CHICKEN PARMI</div>
  <div class="price" style="top:797px;">$30.95</div>
  <div class="item" style="top:860px;">CHICKEN HAWAIIAN PARMI</div>
  <div class="price" style="top:860px;">$30.95</div>
  <div class="item" style="top:923px;">CHICKEN MEATLOVERS PARMI</div>
  <div class="price" style="top:923px;">$30.95</div>
  <div class="item" style="top:986px;">CHICKEN HOT AND SPICY PARMI</div>
  <div class="price" style="top:986px;">$30.95</div>
</div>
</body>
</html>
```